Logistics Website Design

See website https://kravenfreightglobal.com for theme and color details. Need the site to be re-done and reflect some of the designs shown in this list here: https://pixelvane.com/tags/logistics-company-website

Target Market(s)

Logistics & Transportation

Industry/Entity Type

Logistics and Supply Chain

Coding

Coded - Design and coding required

Number of Pages Required

5+ page

Requirements
Must have
• Colors must match theme of logo. Looking for a sleek, interactive design.

```html
<!DOCTYPE html>
<html lang="en">
<head>
<meta charset="utf-8">
<title>Kraven Freight Global — Logistics</title>
<link href="https://fonts.googleapis.com/css2?family=Bebas+Neue&family=Poppins:wght@400;500;600;700&display=swap" rel="stylesheet">
<style>
:root{
  --orange:#e8663c;
  --orange-dark:#c9532e;
  --peach:#fdeee9;
  --peach-card:#fbdccf;
  --ink:#141414;
  --text:#222;
  --white:#fff;
  --grey-circle:#3b3b3b;
}
*{margin:0;padding:0;box-sizing:border-box}
html,body{width:1200px;height:3419px;overflow:hidden}
body{position:relative;background:var(--white);font-family:"Poppins",sans-serif;color:var(--text)}
.abs{position:absolute}
.shapes{position:absolute;left:0;top:0;width:1200px;height:3419px}
.display{font-family:"Bebas Neue",sans-serif;font-weight:400;letter-spacing:.5px}
.btn{position:absolute;background:var(--ink);color:var(--white);font-size:11px;font-weight:600;display:flex;align-items:center;justify-content:center;border-radius:4px;text-transform:uppercase;letter-spacing:.3px;transition:background .25s,transform .25s;cursor:pointer}
.btn:hover{background:var(--orange);transform:translateY(-2px)}

/* hero image area */
.hero-photo{position:absolute;left:0;top:0;width:1200px;height:650px;
  clip-path:path('M0,0 H1200 V568 Q600,672 0,568 Z');
  background:
    linear-gradient(90deg,rgba(15,14,10,.78) 0%,rgba(15,14,10,.45) 32%,rgba(0,0,0,0) 55%),
    radial-gradient(ellipse 120px 190px at 590px 360px,rgba(214,30,36,.9),rgba(214,30,36,0) 100%),
    radial-gradient(ellipse 230px 120px at 650px 220px,rgba(235,235,235,.85),rgba(235,235,235,0) 100%),
    radial-gradient(ellipse 130px 190px at 1040px 290px,rgba(245,245,245,.9),rgba(245,245,245,0) 100%),
    radial-gradient(ellipse 420px 360px at 850px 520px,#6e6f70,rgba(110,111,112,0) 100%),
    linear-gradient(100deg,#2f2a1d 0%,#4d4430 30%,#5a5342 48%,#7b7c78 70%,#8f918f 100%);}
.foot-photo{position:absolute;left:0;top:3050px;width:1200px;height:334px;
  clip-path:path('M0,142 Q600,5 1200,142 V334 H0 Z');
  background:
    linear-gradient(180deg,rgba(20,16,15,.55),rgba(20,16,15,.8)),
    radial-gradient(ellipse 130px 120px at 520px 210px,#7a2320,rgba(122,35,32,0) 100%),
    radial-gradient(ellipse 140px 120px at 860px 200px,#6a6a6a,rgba(106,106,106,0) 100%),
    linear-gradient(90deg,#2a2420,#3a322c 50%,#2c2b2a);}

/* header */
.brand{position:absolute;display:flex;align-items:center;gap:8px;color:var(--white);font-weight:700;font-size:17px}
.brand-dot{width:22px;height:22px;border-radius:50%;background:var(--orange)}
.nav{position:absolute;left:360px;top:29px;width:702px;height:35px;background:var(--orange-dark);border-radius:18px;display:flex;align-items:center;padding-left:31px}
.nav a{color:var(--white);font-size:11px;font-weight:600;text-decoration:none;margin-right:30px;transition:color .2s}
.nav a:hover{color:var(--ink)}
.nav a.active{color:#f7a07f;text-decoration:underline}
.nav-icon{position:absolute;top:5px;width:25px;height:25px;border-radius:50%;background:var(--ink);display:flex;align-items:center;justify-content:center}
.nav-quote{position:absolute;right:6px;top:4px;width:138px;height:27px;background:var(--ink);color:var(--white);border-radius:6px;font-size:11px;font-weight:600;display:flex;align-items:center;justify-content:center}

.hero-title{left:155px;top:196px;font-size:66px;line-height:60px;color:var(--white)}
.hero-sub{left:155px;top:391px;width:300px;font-size:14px;line-height:18px;color:var(--white)}

.section-title{left:0;width:1200px;text-align:center;color:var(--orange);font-size:44px;line-height:40px}
.intro{left:281px;top:815px;width:638px;text-align:center;font-size:12px;line-height:15px;color:var(--ink)}

/* services */
.service-card{position:absolute;top:1109px;width:255px;height:308px;border-radius:12px;transition:transform .3s}
.service-card:hover{transform:translateY(-6px)}
.service-card .photo{position:absolute;inset:0;border-radius:12px;box-shadow:0 8px 20px rgba(0,0,0,.15)}
.service-card .photo::after{content:"";position:absolute;inset:0;border-radius:12px;background:linear-gradient(180deg,rgba(0,0,0,0) 45%,rgba(10,10,10,.85) 80%,#111 100%)}
.service-card h3{position:absolute;left:18px;top:240px;color:var(--white);font-size:19px;font-weight:700;line-height:20px;z-index:1}
.service-card p{position:absolute;left:18px;top:265px;color:var(--white);font-size:13px;font-weight:500;letter-spacing:.3px;z-index:1}
.arrow-circle{position:absolute;width:42px;height:42px;border-radius:50%;background:var(--grey-circle);border:3px solid var(--white);display:flex;align-items:center;justify-content:center;z-index:1;transition:background .25s}
.arrow-circle:hover{background:var(--orange)}
.service-card .arrow-circle{right:32px;top:286px}
.p-flatbed{background:
  radial-gradient(ellipse 90px 60px at 140px 160px,#e9e9e6,rgba(233,233,230,0) 100%),
  radial-gradient(ellipse 70px 130px at 25px 120px,#a4553a,rgba(164,85,58,0) 100%),
  linear-gradient(180deg,#45607f 0%,#7a8ea3 28%,#8a6a52 55%,#4a3d33 100%)}
.p-stepdeck{background:
  radial-gradient(ellipse 70px 70px at 110px 140px,#c23a33,rgba(194,58,51,0) 100%),
  radial-gradient(ellipse 110px 60px at 190px 110px,#8d9198,rgba(141,145,152,0) 100%),
  linear-gradient(180deg,#3e6fb5 0%,#7aa3d8 30%,#6c6f76 60%,#3b3d42 100%)}
.p-dryvan{background:
  radial-gradient(ellipse 110px 60px at 130px 150px,#aeb3b6,rgba(174,179,182,0) 100%),
  linear-gradient(180deg,#2f3338 0%,#5b6169 35%,#74797e 55%,#3c3f42 100%)}
.p-heavy{background:
  radial-gradient(ellipse 100px 70px at 140px 140px,#e0a227,rgba(224,162,39,0) 100%),
  radial-gradient(ellipse 60px 40px at 100px 40px,#8fb6d8,rgba(143,182,216,0) 100%),
  linear-gradient(180deg,#182536 0%,#2c3b4e 35%,#3a3835 65%,#1a1a1a 100%)}

/* about */
.about-photo{left:157px;top:1650px;width:393px;height:463px;border-radius:14px;box-shadow:0 10px 24px rgba(0,0,0,.12);background:
  radial-gradient(ellipse 150px 120px at 230px 290px,#ffffff,rgba(255,255,255,0) 100%),
  radial-gradient(ellipse 90px 140px at 350px 230px,#2a2d31,rgba(42,45,49,0) 100%),
  linear-gradient(160deg,#5f86bc 0%,#a9bdd8 28%,#e6e8eb 46%,#cfd3d8 70%,#9aa0a7 100%)}
.about-title{left:612px;top:1688px;color:var(--orange);font-size:44px;line-height:42px}
.about-text{left:612px;width:420px;font-size:12px;line-height:15px;color:var(--ink)}
.person-card{left:612px;top:1972px;width:413px;height:99px;border-radius:8px;background:var(--peach-card)}
.avatar{position:absolute;left:20px;top:12px;width:76px;height:76px;border-radius:50%;border:3px solid var(--orange);background:linear-gradient(180deg,#eef1f4 0%,#d7dce2 45%,#2f3a4c 100%)}
.person-name{position:absolute;left:119px;top:31px;color:var(--orange);font-size:18px;font-weight:700}
.person-role{position:absolute;left:119px;top:55px;font-size:12px;color:var(--ink)}
.person-card .arrow-circle{left:330px;top:28px;border:none}

/* industries */
.industry{position:absolute;top:2360px;width:160px;text-align:center}
.industry .icon{width:93px;height:93px;margin:0 auto;border-radius:50%;background:var(--white);box-shadow:0 2px 6px rgba(0,0,0,.08);display:flex;align-items:center;justify-content:center;transition:transform .25s,box-shadow .25s}
.industry .icon:hover{transform:scale(1.06);box-shadow:0 6px 14px rgba(232,102,60,.25)}
.industry span{display:block;margin-top:21px;font-size:12.5px;color:var(--ink)}

/* form */
.field{position:absolute;border:1px solid #dcdcdc;background:var(--white);font-size:10px;color:#999;padding:0 12px;display:flex;align-items:center}
.field.area{align-items:flex-start;padding-top:10px}

/* footer */
.foot-head{font-family:"Bebas Neue",sans-serif;color:var(--orange);font-size:17px;letter-spacing:.5px}
.foot-line{display:flex;align-items:flex-start;gap:8px;color:var(--white);font-size:11.5px;line-height:15px}
.foot-links a{display:block;color:var(--white);font-size:11.5px;line-height:18px;text-decoration:none}
.foot-links a.active{color:var(--orange);text-decoration:underline}
.map{left:816px;top:3208px;width:226px;height:123px;border-radius:10px;border:3px solid var(--white);background:
  radial-gradient(ellipse 60px 40px at 160px 40px,#bfe3c8,rgba(191,227,200,0) 100%),
  radial-gradient(ellipse 50px 80px at 200px 100px,#b7d3ee,rgba(183,211,238,0) 100%),
  linear-gradient(135deg,#e6f0e8 0%,#f4f4f2 55%,#dde9f3 100%)}
.bottom-bar{left:0;top:3384px;width:1200px;height:35px;background:var(--orange)}
.copy{left:157px;top:10px;color:var(--white);font-size:11px;font-weight:500}
.social{position:absolute;top:10px;width:14px;height:14px;background:var(--white);border-radius:2px}
</style>
</head>
<body>

<svg class="shapes" viewBox="0 0 1200 3419" aria-hidden="true">
  <path d="M0,568 Q600,724 1200,568 Q600,672 0,568 Z" fill="var(--orange)"/>
  <path d="M0,979 Q600,911 1200,979 V1540 Q600,1606 0,1540 Z" fill="var(--peach)"/>
  <path d="M0,2229 Q600,2163 1200,2229 V2601 Q600,2659 0,2601 Z" fill="var(--peach)"/>
  <path d="M0,3185 Q600,3025 1200,3185 V3419 H0 Z" fill="var(--orange)"/>
</svg>
<div class="hero-photo" role="img" aria-label="Red and white semi trucks driving along a curving forest highway"></div>
<div class="foot-photo" role="img" aria-label="Darkened photo of trucks on a highway"></div>

<!-- header -->
<div class="brand" style="left:166px;top:56px"><span class="brand-dot"></span>Kraven Freight</div>
<nav class="nav">
  <a class="active">HOME</a><a>SERVICES</a><a>INDUSTRIES</a><a>ABOUT US</a><a>CONTACT US</a>
  <span class="nav-icon" style="left:474px"><svg width="11" height="11" viewBox="0 0 24 24"><path d="M6.6 10.8a15 15 0 0 0 6.6 6.6l2.2-2.2c.3-.3.7-.4 1-.2 1.1.4 2.3.6 3.6.6.6 0 1 .4 1 1V20c0 .6-.4 1-1 1A17 17 0 0 1 3 4c0-.6.4-1 1-1h3.5c.6 0 1 .4 1 1 0 1.3.2 2.5.6 3.6.1.3 0 .7-.2 1z" fill="#fff"/></svg></span>
  <span class="nav-icon" style="left:505px"><svg width="11" height="11" viewBox="0 0 24 24"><path d="M3 5h18v14H3z" fill="#fff"/><path d="M3 5l9 7 9-7" stroke="#141414" stroke-width="2" fill="none"/></svg></span>
  <span class="nav-quote">REQUEST A QUOTE</span>
</nav>

<!-- hero -->
<h1 class="abs display hero-title">DELIVERING<br>STRENGTH IN<br>EVERY MILE</h1>
<p class="abs hero-sub">Secure And Reliable Transportation For All Your Cargo Needs.</p>
<div class="btn" style="left:157px;top:447px;width:116px;height:29px">CONTACT NOW</div>

<!-- intro -->
<h2 class="abs display section-title" style="top:718px">KEEPING YOUR SUPPLY<br>CHAIN MOVING</h2>
<p class="abs intro">We Deliver A Comprehensive Range Of Open-Deck And Specialized Transportation Services—Including Flatbed, Step Deck, Heavy Haul, And Over-Dimensional Freight Solutions. Backed By Years Of Experience, A Trusted Nationwide Carrier Network, And A Strong Safety-First Culture, We Provide Reliable, Adaptable Logistics Support Built Around The Unique Requirements Of Every Load.</p>

<!-- services -->
<h2 class="abs display section-title" style="top:1034px">OUR SERVICES</h2>
<div class="service-card" style="left:64px">
  <div class="photo p-flatbed" role="img" aria-label="White truck parked beside stacked shipping containers"></div>
  <h3>FLATBED</h3><p>TRANSPORTATION</p>
  <span class="arrow-circle"><svg width="12" height="12" viewBox="0 0 24 24"><path d="M9 5l7 7-7 7" stroke="#fff" stroke-width="3" fill="none"/></svg></span>
</div>
<div class="service-card" style="left:337px">
  <div class="photo p-stepdeck" role="img" aria-label="Red truck with grey trailer under a blue sky"></div>
  <h3>STEP DECK</h3><p>TRANSPORTATION</p>
  <span class="arrow-circle"><svg width="12" height="12" viewBox="0 0 24 24"><path d="M9 5l7 7-7 7" stroke="#fff" stroke-width="3" fill="none"/></svg></span>
</div>
<div class="service-card" style="left:610px">
  <div class="photo p-dryvan" role="img" aria-label="Grey delivery van outside a glass warehouse"></div>
  <h3>DRY VAN</h3><p>TRANSPORTATION</p>
  <span class="arrow-circle"><svg width="12" height="12" viewBox="0 0 24 24"><path d="M9 5l7 7-7 7" stroke="#fff" stroke-width="3" fill="none"/></svg></span>
</div>
<div class="service-card" style="left:883px">
  <div class="photo p-heavy" role="img" aria-label="Yellow dump truck on a road at night"></div>
  <h3>HEAVY HAUL</h3><p>TRANSPORTATION</p>
  <span class="arrow-circle"><svg width="12" height="12" viewBox="0 0 24 24"><path d="M9 5l7 7-7 7" stroke="#fff" stroke-width="3" fill="none"/></svg></span>
</div>
<div class="btn" style="left:541px;top:1457px;width:118px;height:31px">CONTACT NOW</div>

<!-- about -->
<div class="abs about-photo" role="img" aria-label="White semi truck backed into a loading dock"></div>
<h2 class="abs display about-title">ABOUT US</h2>
<p class="abs about-text" style="top:1755px">Kraven Freight Global™ Was Born Out Of Real-World Experience In The Fitness Equipment Industry. What Started As A Company Shipping Strength Equipment, Cardio Machines, And Training Gear To Gyms, Schools, And Commercial Facilities Quickly Evolved Into Something Bigger.</p>
<p class="abs about-text" style="top:1845px">As Order Volume Grew And Supply Chains Became More Complex, The Team Developed Deep Expertise In Coordinating Freight, Managing Deliveries...</p>
<div class="btn" style="left:612px;top:1911px;width:103px;height:29px">READ MORE</div>
<div class="abs person-card">
  <div class="avatar" role="img" aria-label="Portrait of the director of agency sales"></div>
  <div class="person-name">Darren Okafor,</div>
  <div class="person-role">Director Of Agency Sales</div>
  <span class="arrow-circle"><svg width="12" height="12" viewBox="0 0 24 24"><path d="M9 5l7 7-7 7" stroke="#fff" stroke-width="3" fill="none"/></svg></span>
</div>

<!-- industries -->
<h2 class="abs display section-title" style="top:2280px">OUR INDUSTRIES</h2>
<div class="industry" style="left:186px"><div class="icon"><svg width="42" height="42" viewBox="0 0 42 42" fill="none" stroke="#2d2f7a" stroke-width="2"><rect x="6" y="14" width="14" height="22"/><path d="M20 22h16v14H20"/><path d="M22 22a6 6 0 0 1 12 0" fill="#e8663c"/><path d="M22 28h12"/></svg></div><span>Food &amp; Beverage</span></div>
<div class="industry" style="left:345px"><div class="icon"><svg width="42" height="42" viewBox="0 0 42 42" fill="none" stroke="#2d2f7a" stroke-width="2"><rect x="6" y="8" width="30" height="22" rx="2"/><path d="M21 30v6M14 36h14"/><rect x="16" y="14" width="10" height="10" fill="#e8663c"/></svg></div><span>E-Commerce &amp; Retail</span></div>
<div class="industry" style="left:504px"><div class="icon"><svg width="42" height="42" viewBox="0 0 42 42" fill="none" stroke="#2d2f7a" stroke-width="2"><rect x="6" y="28" width="30" height="6" rx="3"/><rect x="10" y="16" width="8" height="12"/><rect x="24" y="12" width="8" height="16" fill="#e8663c"/></svg></div><span>Manufacturing</span></div>
<div class="industry" style="left:662px"><div class="icon"><svg width="42" height="42" viewBox="0 0 42 42" fill="none" stroke="#2d2f7a" stroke-width="2"><path d="M6 18l10 16h10l10-16"/><circle cx="21" cy="14" r="6" fill="#e8663c"/></svg></div><span>Pharma &amp; Healthcare</span></div>
<div class="industry" style="left:821px"><div class="icon"><svg width="42" height="42" viewBox="0 0 42 42" fill="none" stroke="#2d2f7a" stroke-width="2"><path d="M12 18a9 9 0 0 1 18 0z" fill="#e8663c"/><path d="M8 18h26M10 18v16M16 18v16M21 18v16M26 18v16M32 18v16M6 35h30M21 6v3"/></svg></div><span>Government</span></div>
<div class="btn" style="left:541px;top:2511px;width:118px;height:29px">CONTACT NOW</div>

<!-- quick inquiry -->
<h2 class="abs display section-title" style="top:2714px">QUICK INQUIRY</h2>
<div class="field" style="left:325px;top:2780px;width:268px;height:32px">First Name</div>
<div class="field" style="left:607px;top:2780px;width:268px;height:32px">Last Name</div>
<div class="field" style="left:325px;top:2829px;width:268px;height:32px">Email</div>
<div class="field" style="left:607px;top:2829px;width:268px;height:32px">Phone</div>
<div class="field area" style="left:325px;top:2878px;width:550px;height:80px">How Can We Help?</div>
<div class="btn" style="left:560px;top:2991px;width:80px;height:28px">SUBMIT</div>

<!-- footer -->
<div class="brand" style="left:163px;top:3258px"><span class="brand-dot"></span>Kraven Freight</div>
<div class="abs" style="left:380px;top:3211px">
  <div class="foot-head">CONTACT US</div>
  <div class="foot-line" style="margin-top:8px"><svg width="10" height="10" viewBox="0 0 24 24"><path d="M6.6 10.8a15 15 0 0 0 6.6 6.6l2.2-2.2c.3-.3.7-.4 1-.2 1.1.4 2.3.6 3.6.6.6 0 1 .4 1 1V20c0 .6-.4 1-1 1A17 17 0 0 1 3 4c0-.6.4-1 1-1h3.5c.6 0 1 .4 1 1 0 1.3.2 2.5.6 3.6.1.3 0 .7-.2 1z" fill="#e8663c"/></svg>3015550142</div>
  <div class="foot-line" style="margin-top:13px"><svg width="10" height="10" viewBox="0 0 24 24"><path d="M3 5h18v14H3z" fill="#e8663c"/></svg>sales@kravenfreightglobal.com</div>
  <div class="foot-line" style="margin-top:13px"><svg width="10" height="12" viewBox="0 0 24 28"><path d="M12 0a9 9 0 0 1 9 9c0 7-9 17-9 17S3 16 3 9a9 9 0 0 1 9-9z" fill="#e8663c"/></svg>Lorem Ipsum , Harrow Bay, WA,<br>Australia, 6099</div>
</div>
<div class="abs" style="left:665px;top:3211px">
  <div class="foot-head">QUICK LINKS</div>
  <div class="foot-links" style="margin-top:4px"><a class="active">Home</a><a>Services</a><a>Industries</a><a>About Us</a><a>Contact Us</a></div>
</div>
<div class="abs map" role="img" aria-label="Street map showing the office location"></div>

<div class="abs bottom-bar">
  <div class="abs copy">© 2026 Kraven Freight. All Rights Reserved.</div>
  <span class="social" style="left:971px"></span>
  <span class="social" style="left:999px"></span>
  <span class="social" style="left:1027px"></span>
</div>

</body>
</html>
```